New College Graduate Resume - Creative and unique design that stands out from the rest

Need creative resume design for recent college graduate who graduated from School of Music with a concentration in music composition and production. Striving for a contemporary layout/design that allows the resume to "be unique" and "stand out" but be polished and professional. Open to integrating moderate color/graphics as part of resume design but the design can be minus those attributes as well. Attached is raw content in 7 sections (name/contact info, education, highlights of qualifications, work experience, honors/awards, and professional affiliations). While the designer has full latitude over overall design which (section headers, font type, separation/spacing, use of bullets, justification of text, etc.) please maintain current order/sequence of the 7 sections.

Industry/Entity Type

School

Requirements
Must have
• Name (Tobias Garrick Elwin III) should be most prominent (bold/font size) compared to remainder of resume copy.
• Section headers should be prominent but less so when compared to name on resume.
• The attached file of resume content is provided as raw source copy and is NOT to be just copied and pasted into open fields as is. Expectation is each section of copy will be organized in a manner that is most visually appealing and may include bullets, appropriate spacing, etc.
Should not have
• The attached file of resume content is provided as source copy and is NOT to be just copied and pasted into open fields as is. Expectation is each section of copy will be organized in a manner that

```html
<!DOCTYPE html>
<html lang="en">
<head>
<meta charset="utf-8">
<title>Tobias Garrick Elwin III – Resume</title>
<link href="https://fonts.googleapis.com/css2?family=Roboto+Condensed:wght@400;700&family=Roboto:wght@400&display=swap" rel="stylesheet">
<style>
  :root {
    --navy-deep: #07074a;
    --navy-glow: #2b2b86;
    --accent-red: #b51c24;
    --accent-red-dark: #6e1015;
    --paper: #ffffff;
    --ink: #111111;
    --light: #ffffff;
    --muted: #d8d8ee;
  }
  html, body { margin: 0; padding: 0; overflow: hidden; }
  body { width: 927px; height: 1200px; }
  .resume {
    position: relative;
    width: 927px;
    height: 1200px;
    overflow: hidden;
    background: radial-gradient(ellipse 520px 620px at 250px 330px, var(--navy-glow) 0%, var(--navy-deep) 75%);
    font-family: "Roboto Condensed", "Arial Narrow", sans-serif;
  }
  .name {
    position: absolute;
    left: 74px; top: 62px;
    margin: 0;
    font-size: 40px; font-weight: 700;
    line-height: 46px;
    color: var(--accent-red);
    letter-spacing: 0.6px;
  }
  .contact {
    position: absolute;
    left: 74px; top: 112px;
    margin: 0; padding: 0; list-style: none;
    color: var(--light);
    font-size: 25px; font-weight: 700;
    line-height: 31px;
    letter-spacing: 0.6px;
  }
  .contact li { display: flex; align-items: flex-start; }
  .contact svg { width: 21px; height: 21px; margin: 5px 13px 0 0; flex: none; }
  .profile {
    position: absolute;
    left: 74px; top: 348px;
    width: 192px;
  }
  .profile h2 {
    margin: 0 0 14px;
    font-size: 27px; font-weight: 700;
    line-height: 32px;
    color: var(--accent-red);
  }
  .profile p {
    margin: 0;
    font-family: "Roboto", Arial, sans-serif;
    font-size: 16.5px; line-height: 21.8px;
    letter-spacing: 0.4px;
    color: var(--muted);
  }
  .panel {
    position: absolute;
    left: 336px; top: 320px;
    width: 514px; height: 880px;
    background: var(--paper);
  }
  .section-bar {
    position: absolute;
    left: 27px;
    width: 509px; height: 47px;
    background: var(--accent-red);
    color: var(--light);
    font-size: 26.5px; font-weight: 700;
    line-height: 48px;
    letter-spacing: 0.3px;
    padding-left: 22px; box-sizing: border-box;
    margin: 0;
  }
  .section-bar::after {
    content: "";
    position: absolute;
    right: 0; bottom: -7px;
    border-top: 7px solid var(--accent-red-dark);
    border-right: 22px solid transparent;
  }
  .education-bar { top: 31px; }
  .qualifications-bar { top: 362px; }
  .education {
    position: absolute;
    left: 49px; top: 94px;
    color: var(--ink);
    font-size: 18.5px; font-weight: 700;
    line-height: 23px;
    letter-spacing: 0.8px;
  }
  .education p { margin: 0 0 24px; }
  .qualifications {
    position: absolute;
    left: 49px; top: 428px;
    margin: 0; padding: 0; list-style: none;
    color: var(--ink);
    font-size: 18.5px; font-weight: 700;
    line-height: 27.3px;
    letter-spacing: 0.8px;
  }
  .qualifications li { display: flex; align-items: center; }
  .qualifications li::before {
    content: "";
    width: 0; height: 0;
    border-left: 7px solid var(--accent-red);
    border-top: 6px solid transparent;
    border-bottom: 6px solid transparent;
    margin-right: 6px;
  }
</style>
</head>
<body>
<main class="resume">
  <header>
    <h1 class="name">Tobias Garrick Elwin III</h1>
    <ul class="contact">
      <li>
        <svg viewBox="0 0 20 20" aria-hidden="true"><circle cx="10" cy="10" r="10" fill="#fff"/><path d="M10 4.2a3.6 3.6 0 0 0-3.6 3.6c0 2.7 3.6 7 3.6 7s3.6-4.3 3.6-7A3.6 3.6 0 0 0 10 4.2zm0 5a1.4 1.4 0 1 1 0-2.8 1.4 1.4 0 0 1 0 2.8z" fill="#07074a"/></svg>
        <span>218 Brambleton Court<br>Atlanta, Georgia&nbsp; 30311</span>
      </li>
      <li>
        <svg viewBox="0 0 20 20" aria-hidden="true"><circle cx="10" cy="10" r="10" fill="#fff"/><rect x="6.5" y="4.5" width="7" height="11" rx="1.2" fill="#07074a"/><rect x="7.7" y="6" width="4.6" height="6" fill="#fff"/><circle cx="10" cy="13.8" r="0.8" fill="#fff"/></svg>
        <span>404-555-0187</span>
      </li>
      <li>
        <svg viewBox="0 0 20 20" aria-hidden="true"><circle cx="10" cy="10" r="10" fill="#fff"/><text x="10" y="14" text-anchor="middle" font-family="Arial, sans-serif" font-size="11" font-weight="700" fill="#07074a">@</text></svg>
        <span>tgelwin747@inboxmail.com</span>
      </li>
    </ul>
  </header>

  <aside class="profile">
    <h2>PROFILE</h2>
    <p>Recent graduate of a highly ranked university seeking opportunities to apply composition and production talents across a variety of music genres and other media. Expertise lies in delivering high quality sound design, editing, mixing, and recording. Excellent interpersonal skills and the ability to build strong relationships with people at all levels. Exceptionally motivated self-starter and creative problem solver who enjoys working collaboratively on teams.</p>
  </aside>

  <section class="panel">
    <h2 class="section-bar education-bar">EDUCATION</h2>
    <div class="education">
      <p>Bayshore University – Lindell School of Music<br>Coral Springs, Florida</p>
      <p>Bachelor of Music – May 2016<br>Major: Media Writing and Production, GPA 3.20/4.0</p>
      <p>Hollins Ridge Academy<br>College Park, Georgia<br>High School Diploma with Honors – May 2011</p>
    </div>

    <h2 class="section-bar qualifications-bar">HIGHLIGHTS OF QUALIFICATIONS</h2>
    <ul class="qualifications">
      <li>Media Production Software (TrackForge 11)</li>
      <li>Sound Design</li>
      <li>Sound Acoustics</li>
      <li>Studio Recording</li>
      <li>Audio Editing</li>
      <li>Audio Mixing</li>
      <li>Analog/Digital board operation</li>
      <li>Music Arranging</li>
      <li>Music Composition</li>
      <li>Music Production</li>
      <li>Composing Sheet Music</li>
      <li>Singer-songwriter</li>
      <li>Rhythm guitarist</li>
    </ul>
  </section>
</main>
</body>
</html>
```